Speisekarten-Design für SportsBar
Zielgruppe
Wir sind moderne SportsBar eines 2.Bundesligisten mit breitem Publikum auch ausserhalb der Fussballs. Wir haben Salate, Burger, Schnitzel und Steaks sowie eine gut sortierte Getränkekarte.
Aufgabenstellung
Für unsere Restaurant Ahornstube SportsBar suchen wir eine neue Speisekarte (Alte Speisekarte ist angehängt)
Wir haben uns für das Format A4 im Clipboard entschieden, da wir flexibel sein möchten, auch wenn sich mal etwas ändern sollte, wir somit eine Seite austauschen können. Auch wollen wir mit einer Wochenkarte arbeiten, die auf der zweiten Seite anhängen sollte.
Wir wünschen uns ein sportlich modernes Design, mit Speisefotos und Sportfotos im Mix als Eyecatcher.
Die Seite für den Kaffe wird nicht benötigt, da wir diese von unserem Partner als fertige Vorlage bekommen(Seite hängt an).
Logos der Getränkemarken sind ebenfalls im Anhang. Aller anderen Fotos etc. können sofort bei Bedarf geliefert werden.
Für den ersten Entwurf würde ich gerne 3-5 Seiten sehen wollen, dabei sind wichtig !
- Titelseite
- Brunch & Buffetseite
- Schnitzelseite
- Burgerseite
- Getränke(Bier)
Vielen Dank, für fragen stehe ich jederzeit zur Verfügung

```html
<!DOCTYPE html>
<html lang="de">
<head>
<meta charset="utf-8">
<title>Schnitzel – Ahornstube SportsBar</title>
<link rel="stylesheet" href="https://fonts.googleapis.com/css2?family=Carlito:ital,wght@0,400;1,400&family=Schoolbell&display=swap">
<style>
  :root {
    --slate: #4d6585;
    --slate-dark: #3c5272;
    --slate-light: #5f7898;
    --band: #e6e7e9;
    --ink: #2f3238;
    --text: #f3f5f8;
    --text-soft: #dfe5ee;
    --fries: #e9a53a;
    --crumb: #b9772e;
    --plate: #efece6;
  }
  * { margin: 0; padding: 0; box-sizing: border-box; }
  html, body { width: 848px; height: 1200px; overflow: hidden; }
  body { font-family: "Carlito", "Calibri", sans-serif; color: var(--text); }
  .menu-page {
    position: relative; width: 848px; height: 1200px; overflow: hidden;
    background:
      radial-gradient(ellipse at 30% 20%, var(--slate-light) 0%, transparent 55%),
      radial-gradient(ellipse at 80% 70%, var(--slate-dark) 0%, transparent 60%),
      var(--slate);
  }
  .title-band {
    position: absolute; left: 0; top: 65px; width: 848px; height: 72px;
    background: var(--band);
    display: flex; align-items: center; justify-content: center;
  }
  .title-band h1 {
    font-family: "Schoolbell", cursive; font-weight: 400;
    font-size: 38px; color: var(--ink); letter-spacing: 1px;
  }
  .dish-list { position: absolute; left: 40px; top: 162px; width: 762px; list-style: none; }
  .dish { height: 51.3px; display: grid; grid-template-columns: 1fr auto; }
  .dish.spaced { margin-top: 8px; }
  .dish-name { font-size: 15px; line-height: 20px; }
  .dish-price { font-size: 15px; line-height: 20px; text-align: right; }
  .dish-desc { grid-column: 1 / 2; font-style: italic; font-size: 14px; line-height: 20px; color: var(--text-soft); }
  .extras { position: absolute; left: 40px; top: 922px; width: 762px; list-style: none; }
  .extras li { display: flex; justify-content: space-between; font-size: 15px; line-height: 20.5px; }
  .sides-note {
    position: absolute; left: 0; top: 1006px; width: 848px; text-align: center;
    font-family: "Schoolbell", cursive; font-size: 14px; color: var(--text);
  }
  .divider { position: absolute; left: 0; top: 1029px; width: 848px; height: 1px; background: var(--text); }
  .food-photo {
    position: absolute; left: 0; top: 1046px; width: 848px; height: 154px;
    background:
      radial-gradient(ellipse at 78% 10%, #f5d45a 0%, transparent 18%),
      linear-gradient(100deg, var(--fries) 0%, #f0b54b 38%, var(--crumb) 58%, #c98a3c 85%, var(--plate) 100%);
  }
</style>
</head>
<body>
<main class="menu-page">
  <header class="title-band"><h1>Schnitzel</h1></header>

  <ul class="dish-list">
    <li class="dish"><span class="dish-name">Schnitzel -natur-</span><span class="dish-price">9,80€</span><span class="dish-desc">mit Kräutebutter</span></li>
    <li class="dish"><span class="dish-name">Schnitzel „Wiener Art“</span><span class="dish-price">10,50€</span><span class="dish-desc">In goldgelber Panade mit frischer Zitrone</span></li>
    <li class="dish"><span class="dish-name">Rahmschnitzel</span><span class="dish-price">10,90€</span><span class="dish-desc">In rahmiger Sahnesoße</span></li>
    <li class="dish"><span class="dish-name">Schnitzel „Pfefferrahm“</span><span class="dish-price">11,50€</span><span class="dish-desc">Mit frischem Pfeffer in leckerer Sahnesoße</span></li>
    <li class="dish"><span class="dish-name">Zwiebelschnitzel</span><span class="dish-price">11,50€</span><span class="dish-desc">In herzhafter Zwiebelsoße</span></li>
    <li class="dish"><span class="dish-name">Feuerschnitzel</span><span class="dish-price">11,50€</span><span class="dish-desc">In feuriger Tomaten-Chili Soße</span></li>
    <li class="dish"><span class="dish-name">Schnitzel Crema</span><span class="dish-price">11,80€</span><span class="dish-desc">Herzhafter Käse meets Sahnesoße</span></li>
    <li class="dish"><span class="dish-name">Schnitzel „Champignon-Rahm“</span><span class="dish-price">12,50€</span><span class="dish-desc">Mit frischen Champignons in Sahnesoße</span></li>
    <li class="dish"><span class="dish-name">Schnitzel „Bölle“</span><span class="dish-price">12,50€</span><span class="dish-desc">Kleingehackte Zwiebeln, Paprika, Champignons und Knoblauch in Sahnesoße</span></li>
    <li class="dish"><span class="dish-name">Bologneseschnitzel</span><span class="dish-price">12,50€</span><span class="dish-desc">In würziger Tomaten-Hackfleischsoße</span></li>
    <li class="dish"><span class="dish-name">Ahornschnitzel</span><span class="dish-price">12,50€</span><span class="dish-desc">Mit knusprigen Speck, Zwiebeln und Spiegelei</span></li>
    <li class="dish"><span class="dish-name">Kochkäs-Schnitzel</span><span class="dish-price">12,50€</span><span class="dish-desc">Mit selbstgemachtem Kochkäse zubereitet</span></li>
    <li class="dish"><span class="dish-name">Cordon-Bleu</span><span class="dish-price">13,50€</span><span class="dish-desc">Gefüllt mit herzhaftem Käse und Schinken</span></li>
    <li class="dish spaced"><span class="dish-name">Ahorn Cordon-Bleu</span><span class="dish-price">14,50€</span><span class="dish-desc">Schnitzel meets Bolognesesoße auf Sauce Hollandaise und Käse überbacken</span></li>
  </ul>

  <ul class="extras">
    <li><span>Alle Schnitzel auch als paniertes Putenschnitzel erhältlich</span><span>+ 1€</span></li>
    <li><span>Alle Schnitzel auch als XXL!</span><span>+ 3€</span></li>
  </ul>

  <p class="sides-note">Alle Schnitzel wahlweise mit Wedges, SportsBar Fries oder Bratkartoffeln &amp; Salat</p>
  <div class="divider"></div>

  <div class="food-photo" role="img" aria-label="Foto: paniertes Schnitzel mit Zitronenscheibe und Pommes frites"></div>
</main>
</body>
</html>
```